Corvell Lending Partners. Professional and Established Company

A full service finance company specializing in obtaining capital for small business. Business Lending advisor, helping small business owners access the capital they need to launch, grow, or sustain their business. Many of our programs offer flexible guidelines to overcome common obstacles such as credit score, credit history, and time in business, financials, and industry type. Our streamlined funding process makes getting a business loan, business line of credit, stated income commercial real estate loan, a smooth and stress free experience.SOME OF THE MOST COMMON NEEDS FOR BUSINESS CAPITAL:• Working Capital• Debt Consolidations (loans, merchant cash advances, etc.)• Payroll• Operating Expenses• Inventory• Equipment Financing• Commercial Real Estate (Purchase, Fix & Flip, Rehab, Renovations)• Business Acquisitions• Business ExpansionWe like the websites:www.brandtwoodfc.com they are in the same industry and provide the same servicesWe are wanting to be able to update when we do press releases and such using Word Press. Our look should be very professional and we will be adding Our Team Professional Bios and Headshots.

Industry/Entity Type

Finance

Number of Pages Required

5+ page

Font styles to use
Serif
Sans Serif

Requirements
Must have
• We want to copy brandtwoodfc.com
• We need:
• Home Page
• About Us
• Loan Programs
• Loan Criteria
• News
• Apply Now
• Contact
Nice to have
• See brandtwoodfc.com
Should not have
• Need professional design. Nothing bright or abstract

```html
<!DOCTYPE html>
<html lang="en">
<head>
<meta charset="utf-8">
<title>Corvell Lending Partners</title>
<link href="https://fonts.googleapis.com/css2?family=Montserrat:wght@400;500;600;700&display=swap" rel="stylesheet">
<style>
:root{
  --blue:#3a78bd;
  --blue-dark:#2b5f9e;
  --blue-soft:#5b9bd8;
  --ink:#3d3d3d;
  --muted:#777;
  --pale:#efeff0;
  --footer:#0d0f15;
  --white:#fff;
}
*{margin:0;padding:0;box-sizing:border-box}
html,body{width:1200px;height:3616px;overflow:hidden;background:var(--white)}
body{font-family:"Montserrat",Arial,sans-serif;color:var(--ink);position:relative}
.abs{position:absolute}
.center{text-align:center;left:0;width:1200px}

/* header */
.brand{left:136px;top:17px;font-weight:700;font-size:17px;color:var(--blue);line-height:21px;width:170px;letter-spacing:.3px}
.contact{top:30px;font-size:12px;color:#888;display:flex;align-items:center;gap:8px;white-space:nowrap}
.contact svg{width:12px;height:12px;fill:var(--blue)}
.apply{left:946px;top:24px;width:118px;height:28px;background:var(--blue);color:var(--white);font-size:11px;font-weight:600;display:flex;align-items:center;justify-content:center}
.nav{top:76px;left:0;width:1200px;height:49px;background:var(--blue);display:flex;gap:17px;padding-left:137px;align-items:center}
.nav a{color:var(--white);font-size:11px;font-weight:500;text-decoration:none}

/* hero */
.hero{top:125px;left:0;width:1200px;height:587px;background:linear-gradient(180deg,#5a7aa3 0%,#7c97b8 45%,#5d7595 100%);clip-path:polygon(0 0,100% 0,100% 493px,0 587px)}
.hero-title{top:240px;font-size:46px;font-weight:700;color:var(--white);line-height:54px}
.hero-text{top:364px;font-size:11.5px;color:var(--white);line-height:20px}
.arrow{top:340px;width:20px;height:20px}
.arrow path{stroke:var(--white);stroke-width:1.6;fill:none}
.stat{top:508px;width:190px;text-align:center;color:var(--white)}
.stat .k{font-size:10px;letter-spacing:2.5px;font-weight:600}
.stat .v{font-size:15px;font-weight:600;letter-spacing:1px;margin-top:5px}
.stat .s{font-size:9px;font-style:italic;line-height:18px;margin-top:4px}
.stat-rule{top:510px;width:1px;height:86px;background:rgba(255,255,255,.5)}

/* programs */
.pale{left:0;top:620px;width:1200px;height:950px;background:var(--pale)}
.section-title{font-size:24px;font-weight:700;color:#4a4a4a}
.card{width:296px;height:150px;overflow:hidden}
.card .photo{position:absolute;inset:0}
.card .cap{position:absolute;left:0;bottom:0;width:100%;height:31px;background:rgba(58,120,189,.9);color:var(--white);font-size:12.5px;font-weight:600;padding:9px 12px}
.card.featured{background:linear-gradient(180deg,#3f7cc0,#5c94cc);color:var(--white);text-align:center}
.card.featured h3{font-size:12.5px;font-weight:600;margin-top:14px}
.card.featured p{font-size:11px;line-height:19px;margin:30px 22px 0}
.btn-outline{left:453px;top:1382px;width:298px;height:44px;border:2px solid #9bb6d6;color:var(--blue);font-size:11px;font-weight:600;display:flex;align-items:center;justify-content:center;background:var(--white)}

/* advisor */
.advisor{left:0;top:1461px;width:1200px;height:616px;background:linear-gradient(100deg,#3e7fc4 0%,#4f92d4 55%,#6ea9de 100%);clip-path:polygon(0 69px,100% 0,100% 549px,0 616px)}
.advisor-title{left:282px;top:1650px;font-size:33px;font-weight:700;color:var(--white);line-height:48px;white-space:nowrap}
.advisor-text{left:288px;top:1758px;width:600px;font-size:11px;line-height:20px;color:var(--white)}
.video-btn{left:293px;top:1871px;width:245px;height:45px;border:2px solid var(--white);color:var(--white);font-size:11px;font-weight:600;letter-spacing:2px;display:flex;align-items:center;justify-content:center;gap:16px}

/* team */
.sub{font-size:13px;color:#555;line-height:25px}
.member{width:188px;height:226px;border-radius:4px;background:linear-gradient(180deg,#d9d9d9,#8f8f8f)}
.member.lead{width:209px;height:251px;border-radius:0;border-bottom:3px solid var(--blue)}
.name{width:240px;text-align:center;font-size:14px;font-weight:500;color:#444}
.bio{width:240px;text-align:center;font-size:11px;line-height:21px;color:#666}
.dot{width:10px;height:10px;border-radius:50%;background:#bbb;top:2666px}
.dot.on{width:13px;height:13px;background:var(--blue);top:2664px}

/* blog */
.blog-bg{left:0;top:2697px;width:1200px;height:600px;background:var(--pale);clip-path:polygon(0 64px,100% 0,100% 100%,0 100%)}
.post{width:291px;height:277px;background:var(--white);border:1px solid #ddd}
.post .img{height:161px;background:linear-gradient(160deg,#4b78b0,#9fb9d6)}
.post h4{font-size:11px;font-weight:600;margin:28px 18px 0;color:#333}
.post p{font-size:10.5px;line-height:19px;color:#666;margin:6px 18px 0}

/* footer */
.footer{left:0;top:3239px;width:1200px;height:377px;background:var(--footer);clip-path:polygon(0 52px,100% 0,100% 100%,0 100%)}
.f-brand{left:161px;top:3394px;font-size:15px;font-weight:700;color:var(--blue-soft);width:170px;line-height:20px}
.f-head{top:3366px;font-size:11px;font-weight:700;color:var(--white);letter-spacing:.5px}
.f-item{font-size:11.5px;color:#cfd3da;line-height:24px;white-space:nowrap}
.f-icon{width:13px;height:13px;fill:var(--white)}
.social{top:3397px;width:24px;height:24px}
.copy{top:3584px;font-size:9px;color:#555}
</style>
</head>
<body>

<!-- header -->
<div class="abs brand">Corvell Lending Partners</div>
<div class="abs contact" style="left:648px">
  <svg viewBox="0 0 24 24"><path d="M6.6 10.8a15 15 0 0 0 6.6 6.6l2.2-2.2c.3-.3.7-.4 1-.2 1.1.4 2.3.6 3.6.6.6 0 1 .4 1 1V20c0 .6-.4 1-1 1A17 17 0 0 1 3 4c0-.6.4-1 1-1h3.5c.6 0 1 .4 1 1 0 1.3.2 2.5.6 3.6.1.3 0 .7-.2 1z"/></svg>
  01632 960 418
</div>
<div class="abs contact" style="left:781px">
  <svg viewBox="0 0 24 24"><path d="M2 5h20v14H2z M2 5l10 8 10-8" fill="none" stroke="#3a78bd" stroke-width="2.4"/></svg>
  contact@corvell.com
</div>
<div class="abs apply">APPLY NOW</div>
<nav class="abs nav">
  <a>ABOUT US</a><a>LOAN PROGRAMS</a><a>LOAN CLOSINGS</a><a>LOAN CRITERIA</a><a>NEWS</a><a>CONTACT US</a>
</nav>

<!-- hero -->
<div class="abs hero" role="img" aria-label="Upward view of glass skyscrapers against the sky"></div>
<div class="abs center hero-title">FULL SERVICE<br>FINANCE COMPANY</div>
<div class="abs center hero-text">Business Lending advisor, helping small business owners access the capital they need to launch, grow, or<br>sustain their business. Many of our programs offer flexible guidelines to overcome.</div>
<svg class="abs arrow" style="left:95px" viewBox="0 0 20 20"><path d="M13 2 5 10l8 8"/></svg>
<svg class="abs arrow" style="left:1079px" viewBox="0 0 20 20"><path d="M7 2l8 8-8 8"/></svg>

<div class="abs stat" style="left:123px"><div class="k">MIXED-USE</div><div class="v">$15,000,000</div><div class="s">TOWNHOUSE<br>MANHATTAN, NY</div></div>
<div class="abs stat-rule" style="left:308px"></div>
<div class="abs stat" style="left:315px"><div class="k">MIXED-USE</div><div class="v">$15,000,000</div><div class="s">TOWNHOUSE<br>MANHATTAN, NY</div></div>
<div class="abs stat-rule" style="left:508px"></div>
<div class="abs stat" style="left:510px"><div class="k">MIXED-USE</div><div class="v">$15,000,000</div><div class="s">TOWNHOUSE<br>MANHATTAN, NY</div></div>
<div class="abs stat-rule" style="left:708px"></div>
<div class="abs stat" style="left:702px"><div class="k">MIXED-USE</div><div class="v">$15,000,000</div><div class="s">TOWNHOUSE<br>MANHATTAN, NY</div></div>
<div class="abs stat-rule" style="left:908px"></div>
<div class="abs stat" style="left:906px"><div class="k">MIXED-USE</div><div class="v">$15,000,000</div><div class="s">TOWNHOUSE<br>MANHATTAN, NY</div></div>

<!-- loan programs -->
<div class="abs pale"></div>
<div class="abs center section-title" style="top:762px">LOAN PROGRAMS</div>

<div class="abs card featured" style="left:133px;top:831px">
  <h3>LAND LOAN</h3>
  <p>We are one of a select few private lenders to specialize in land loans...few private lenders to specialize in land loans..</p>
</div>
<div class="abs card" style="left:453px;top:831px"><div class="photo" role="img" aria-label="Hotel reception desk with guest checking in" style="background:linear-gradient(135deg,#6b4a32,#c9a57c)"></div><div class="cap">HOSPITALITY LOANS</div></div>
<div class="abs card" style="left:770px;top:831px"><div class="photo" role="img" aria-label="Apartment complex with swimming pool" style="background:linear-gradient(180deg,#c9d7e6,#b0584f 55%,#3aa6d9)"></div><div class="cap">MULTIFAMILY LOANS</div></div>

<div class="abs card" style="left:133px;top:1012px"><div class="photo" role="img" aria-label="Bright empty office interior" style="background:linear-gradient(180deg,#e8ecef,#aab4bb)"></div><div class="cap">OFFICE LOANS</div></div>
<div class="abs card" style="left:453px;top:1012px"><div class="photo" role="img" aria-label="Lit mixed-use building at dusk" style="background:linear-gradient(180deg,#2c3f86,#6a6fb8 60%,#d9a860)"></div><div class="cap">MIXED-USE LOANS</div></div>
<div class="abs card" style="left:770px;top:1012px"><div class="photo" role="img" aria-label="Shopping mall interior with shoppers" style="background:linear-gradient(180deg,#d8d4cc,#8c6f5a)"></div><div class="cap">RETAIL LOANS</div></div>

<div class="abs card" style="left:133px;top:1194px"><div class="photo" role="img" aria-label="Industrial plant at sunset" style="background:linear-gradient(180deg,#8a7fb5,#d6967a 55%,#3d4a66)"></div><div class="cap">INDUSTRIAL LOANS</div></div>
<div class="abs card" style="left:453px;top:1194px"><div class="photo" role="img" aria-label="Warehouse racks with boxes" style="background:linear-gradient(135deg,#8a5a3a,#c48e5c 50%,#3a4b6b)"></div><div class="cap">WAREHOUSE LOANS</div></div>
<div class="abs card" style="left:770px;top:1194px"><div class="photo" role="img" aria-label="Row of self storage units with blue doors" style="background:linear-gradient(180deg,#5b8fd1,#e9edf2 60%,#c7ccd2)"></div><div class="cap">SELF STORAGE LOANS</div></div>

<div class="abs btn-outline">VIEW LOAN PROGRAMS</div>

<!-- advisor -->
<div class="abs advisor" role="img" aria-label="Person working on a laptop, blue tinted"></div>
<h2 class="abs advisor-title">BEST FINANCIAL ADVISOR FOR<br>YOUR BUSINESS&nbsp; TO GROWUP</h2>
<p class="abs advisor-text">A full service finance company specializing in obtaining capital for small business. Business Lending advisor, helping small business owners access the capital they need to launch, grow, or sustain their business. Many of our programs offer flexible guidelines to overcome common obstacles such as credit score, credit history, and time in business, financials.</p>
<div class="abs video-btn">
  <svg width="20" height="20" viewBox="0 0 20 20"><circle cx="10" cy="10" r="8.5" fill="none" stroke="#fff" stroke-width="1.5"/><path d="M8 6.5v7l5.5-3.5z" fill="#fff"/></svg>
  WATCH VIDEO
</div>

<!-- team -->
<div class="abs center section-title" style="top:2124px">OUR TEAM</div>
<div class="abs center sub" style="top:2162px">Sed ut perspiciatis unde omnis iste natus error sit<br>voluptatem accusantium doloremque laudantium totam rem</div>

<div class="abs member" style="left:159px;top:2286px" role="img" aria-label="Black and white headshot of Catherine Vale"></div>
<div class="abs member lead" style="left:382px;top:2261px" role="img" aria-label="Colour headshot of Harold Rusk in suit"></div>
<div class="abs member" style="left:626px;top:2286px" role="img" aria-label="Black and white headshot of Janine Price"></div>
<div class="abs member" style="left:860px;top:2286px" role="img" aria-label="Black and white headshot of Keaton Walsh"></div>

<div class="abs name" style="left:133px;top:2538px">CATHERINE VALE</div>
<div class="abs bio" style="left:133px;top:2563px">Ut enim ad minim veniam, quis<br>nostrud exercitation ullamco laboris</div>
<div class="abs name" style="left:366px;top:2538px">HAROLD RUSK</div>
<div class="abs bio" style="left:366px;top:2563px">Nemo enim ipsam voluptatem quia<br>voluptas sit aspernatur aut odit aut</div>
<div class="abs name" style="left:600px;top:2538px">JANINE PRICE</div>
<div class="abs bio" style="left:600px;top:2563px">Commodo consequat. Duis aute irure<br>dolor in reprehenderit in voluptate</div>
<div class="abs name" style="left:834px;top:2538px">KEATON WALSH</div>
<div class="abs bio" style="left:834px;top:2563px">Velit esse cillum dolore eu fugiat nulla<br>pariatur. Excepteur sint occaecat</div>

<div class="abs dot" style="left:561px"></div>
<div class="abs dot on" style="left:585px"></div>
<div class="abs dot" style="left:610px"></div>
<div class="abs dot" style="left:635px"></div>

<!-- blog -->
<div class="abs blog-bg"></div>
<div class="abs center section-title" style="top:2800px">FROM THE BLOG</div>
<div class="abs center sub" style="top:2834px;font-size:11px;line-height:20px">Said open land form moved air his signs moveth creepeth appear appear it. Appear<br>living you dry our tree one.</div>

<article class="abs post" style="left:135px;top:2916px">
  <div class="img" role="img" aria-label="Business team shaking hands in office"></div>
  <h4>The most well-known dummy text is the</h4>
  <p>Said open land form moved air his signs moveth creepeth appear appear it. Appear living you dry our tree one.</p>
</article>
<article class="abs post" style="left:452px;top:2916px">
  <div class="img" role="img" aria-label="Man in glasses reading a tablet"></div>
  <h4>The most well-known dummy text is the</h4>
  <p>Said open land form moved air his signs moveth creepeth appear appear it. Appear living you dry our tree one.</p>
</article>
<article class="abs post" style="left:773px;top:2916px">
  <div class="img" role="img" aria-label="Hands reviewing financial charts on desk"></div>
  <h4>The most well-known dummy text is the</h4>
  <p>Said open land form moved air his signs moveth creepeth appear appear it. Appear living you dry our tree one.</p>
</article>

<!-- footer -->
<footer class="abs footer"></footer>
<div class="abs f-brand">Corvell Lending Partners</div>

<div class="abs f-head" style="left:372px">GET IN TOUCH</div>
<svg class="abs f-icon" style="left:372px;top:3402px" viewBox="0 0 24 24"><rect x="6" y="1" width="12" height="22" rx="2" fill="none" stroke="#fff" stroke-width="2.5"/></svg>
<div class="abs f-item" style="left:401px;top:3396px">555-014-2290</div>
<svg class="abs f-icon" style="left:372px;top:3438px" viewBox="0 0 24 24"><path d="M22 2 2 10l9 3 3 9z"/></svg>
<div class="abs f-item" style="left:401px;top:3432px">42 Alder Row</div>
<div class="abs f-item" style="left:401px;top:3461px">Fairbrook 0421 Examplia</div>
<svg class="abs f-icon" style="left:372px;top:3497px" viewBox="0 0 24 24"><path d="M2 5h20v14H2z"/><path d="M2 5l10 8 10-8" fill="none" stroke="#0d0f15" stroke-width="2"/></svg>
<div class="abs f-item" style="left:401px;top:3490px">hello@corvell.com</div>

<div class="abs f-head" style="left:648px">USEFUL LINKS</div>
<div class="abs f-item" style="left:648px;top:3393px;font-size:11px">About us<br>Loan Programs<br>Loan Closings<br>Loan Criteria<br>News<br>Contact</div>

<div class="abs f-head" style="left:860px">FOLLOW US</div>
<div class="abs social" style="left:860px;background:#3d9ae0"></div>
<div class="abs social" style="left:901px;background:#3b5a9a"></div>
<div class="abs social" style="left:942px;background:#d9493b"></div>
<div class="abs social" style="left:983px;background:#d8272a"></div>

<div class="abs center copy">Copyright 2018 corvell.com. All rights reserved</div>

</body>
</html>
```